Cool modern, tech Business card design

Looking for a new business card design for our Managed IT Services company. We would like 2 sides, with the logo one one side horizontally and then the information on the back in either vertical or horizontal. We want our colors from the logo incorporated but also would like to see the color gray in there as well.

Target Market(s)

IT, Information Technology, Tech, Service

Industry/Entity Type

It Service

Contact Information for Business Card

Carl Penner
Managing Partner
(P)555-271-4830 ext xxx
(F)555-271-4831
www.brixtelcore.com

Font styles to use
Sans Serif

Colors
959595
000000
ec1f27

Requirements
Must have
• Logo on one side with some nice design or pattern
• Information on back in either vertical or horizontal format
Nice to have
• For it to look cool, tech, modern, stand out.

```html
<!DOCTYPE html>
<html lang="en">
<head>
<meta charset="utf-8">
<title>Brixtelcore — Business Card</title>
<link href="https://fonts.googleapis.com/css2?family=Montserrat:wght@400;500&display=swap" rel="stylesheet">
<style>
  :root {
    --bg: #5a5a5b;
    --paper: #ffffff;
    --ink: #231f20;
    --dark: #161616;
    --red: #ec1f27;
    --red-soft: #f28a8c;
    --grey: #959595;
    --light-text: #d6d6d6;
  }
  html, body {
    margin: 0;
    width: 1200px;
    height: 1200px;
    overflow: hidden;
    background: var(--bg);
    font-family: "Montserrat", Arial, sans-serif;
  }
  .stage {
    position: relative;
    width: 1174px;
    height: 1174px;
    transform: scale(1.0222);
    transform-origin: 0 0;
  }
  .card {
    position: absolute;
    overflow: hidden;
    background: var(--paper);
  }
  .card--front { left: 230px; top: 103px; width: 714px; height: 408px; }
  .card--back  { left: 229px; top: 655px; width: 716px; height: 407px; }
  .card svg.waves { position: absolute; inset: 0; }

  .wordmark {
    position: absolute;
    display: flex;
    align-items: center;
    gap: 10px;
    font-weight: 500;
    letter-spacing: -0.5px;
    white-space: nowrap;
  }
  .wordmark__mark { width: 16px; height: 16px; background: var(--red); }
  .card--front .wordmark {
    left: 0; right: 0; top: 148px;
    justify-content: center;
    font-size: 42px;
    color: var(--ink);
  }
  .card--back .wordmark {
    right: 62px; top: 308px;
    font-size: 28px;
    color: var(--paper);
  }
  .card--back .wordmark__mark { width: 12px; height: 12px; }

  .person { position: absolute; left: 59px; top: 50px; }
  .person__name {
    margin: 0;
    font-size: 30px;
    font-weight: 400;
    color: var(--ink);
    letter-spacing: 0.5px;
    line-height: 1;
  }
  .person__role {
    margin: 5px 0 0;
    font-size: 11.5px;
    font-weight: 500;
    color: #3a3a3a;
    letter-spacing: 0.5px;
  }

  .contacts {
    position: absolute;
    left: 62px; top: 245px;
    margin: 0; padding: 0;
    list-style: none;
  }
  .contacts li {
    display: flex;
    align-items: center;
    height: 32px;
    margin-bottom: 18.5px;
    font-size: 18px;
    color: var(--light-text);
    letter-spacing: 0.3px;
  }
  .contacts__icon {
    width: 32px; height: 32px;
    border-radius: 5px;
    background: var(--red);
    margin-right: 21px;
    display: flex; align-items: center; justify-content: center;
  }
  .contacts__icon svg { width: 18px; height: 18px; }
</style>
</head>
<body>
<main class="stage">

  <section class="card card--front" aria-label="Card front">
    <svg class="waves" viewBox="0 0 714 408" preserveAspectRatio="none" aria-hidden="true">
      <defs>
        <linearGradient id="ribbon-front" x1="0" x2="1" y1="0" y2="0">
          <stop offset="0" stop-color="var(--red-soft)"/>
          <stop offset="0.3" stop-color="var(--red)"/>
          <stop offset="0.55" stop-color="#f47a7c"/>
          <stop offset="0.75" stop-color="var(--red)"/>
          <stop offset="1" stop-color="var(--red)"/>
        </linearGradient>
      </defs>
      <path fill="url(#ribbon-front)"
        d="M0 224 C60 222 150 222 250 268 C330 305 400 332 480 318 C560 304 600 262 700 256 L714 266
           L714 303 C640 285 580 290 500 318 C430 340 350 338 280 308 C200 274 120 262 0 262 Z"/>
    </svg>
    <div class="wordmark"><span>brixtelcore</span><span class="wordmark__mark"></span></div>
  </section>

  <section class="card card--back" aria-label="Card back">
    <svg class="waves" viewBox="0 0 716 407" preserveAspectRatio="none" aria-hidden="true">
      <defs>
        <linearGradient id="ribbon-back" x1="0" x2="1" y1="0" y2="0">
          <stop offset="0" stop-color="var(--red-soft)"/>
          <stop offset="0.3" stop-color="var(--red)"/>
          <stop offset="0.5" stop-color="#f26466"/>
          <stop offset="0.8" stop-color="var(--red)"/>
        </linearGradient>
      </defs>
      <path fill="url(#ribbon-back)"
        d="M0 150 C90 138 180 150 260 166 C340 180 420 176 500 140 C580 102 640 74 716 74
           L716 114 C640 108 580 118 520 142 C440 176 360 206 260 200 C170 194 90 178 0 192 Z"/>
      <path fill="var(--dark)"
        d="M0 192 C90 178 170 194 260 200 C360 206 440 176 520 142 C580 118 640 108 716 114 L716 407 L0 407 Z"/>
    </svg>

    <div class="person">
      <h1 class="person__name">CARL PENNER</h1>
      <p class="person__role">MANAGING PARTNER</p>
    </div>

    <ul class="contacts">
      <li>
        <span class="contacts__icon">
          <svg viewBox="0 0 24 24" fill="#fff" aria-hidden="true"><path d="M3 8c0-2 4-4 9-4s9 2 9 4v2h-5V8.5c-1-.6-2.4-.9-4-.9s-3 .3-4 .9V10H3z"/><path d="M6 11h12l2 8H4z"/><circle cx="12" cy="15" r="2.2" fill="var(--red)"/></svg>
        </span>
        555-271-4830 Ext: xxx
      </li>
      <li>
        <span class="contacts__icon">
          <svg viewBox="0 0 24 24" fill="none" stroke="#fff" stroke-width="1.6" aria-hidden="true"><path d="M8 3h6l3 3v8H8z"/><rect x="4" y="14" width="16" height="7"/><path d="M10 8h5M10 11h5"/></svg>
        </span>
        555-271-4831
      </li>
      <li>
        <span class="contacts__icon">
          <svg viewBox="0 0 24 24" fill="none" stroke="#fff" stroke-width="1.5" aria-hidden="true"><circle cx="12" cy="12" r="9"/><ellipse cx="12" cy="12" rx="4" ry="9"/><path d="M3 12h18M5 7h14M5 17h14"/></svg>
        </span>
        www.brixtelcore.com
      </li>
    </ul>

    <div class="wordmark"><span>brixtelcore</span><span class="wordmark__mark"></span></div>
  </section>

</main>
</body>
</html>
```